Premium modern eliquids labels 84.5 x 80 mm

I am looking for modern graphics for the labels of a new eliquid line that will have 4 different types of eliquids. It will have a tobacco one (brown colours maybe), a fruity one (bright colours maybe), a minty one (green colours maybe) and a creamy one (beige colours maybe).
I will need one of them to see how the design is, that design will have to be adapted to the other 3 colours of the label.
The brand logo is attached. I also attached a sample of what is mandatory to write on the label, you can change size, place and font of what is written, the only thing that cannot be reduced is the yellow parts. I attach the bottle that we will use.The size of the label is 84.5 x 80 mm (base x height).

Target Market(s)

vapers

Requirements
Must have
• My project must have one of the labels.

```html
<!DOCTYPE html>
<html lang="it">
<head>
<meta charset="utf-8">
<title>Solenne Aroma – Tobacco e-liquid label</title>
<link rel="stylesheet" href="https://fonts.googleapis.com/css2?family=Montserrat:wght@300;400;700&family=Archivo+Black&display=swap">
<style>
  :root {
    --page: #ffffff;
    --brown-dark: #5a2b1e;
    --brown-mid: #a8533a;
    --brown-soft: #8a4430;
    --caramel: #e9a86a;
    --ink-light: #ffffff;
    --badge-yellow: #f7c234;
    --badge-ink: #1a1a1a;
  }
  * { margin: 0; padding: 0; box-sizing: border-box; }
  html, body {
    width: 1200px; height: 1200px; overflow: hidden;
    background: var(--page);
  }
  .label {
    position: absolute; left: 50px; top: 87px;
    width: 1100px; height: 1026px;
    background: var(--brown-dark);
    overflow: hidden;
    font-family: 'Montserrat', sans-serif;
    color: var(--ink-light);
  }
  .flavour-art { position: absolute; left: 0; top: 0; width: 1100px; height: 1026px; }
  .info-block {
    position: absolute; font-size: 24px; line-height: 29.5px; font-weight: 400;
    letter-spacing: 0.2px;
  }
  .ingredients { left: 12px; top: 20px; }
  .instructions { left: 918px; top: 20px; width: 182px; }
  .producer { left: 12px; top: 786px; }
  .lot-code {
    position: absolute; left: 41px; top: 483px;
    transform: translate(-50%, -50%) rotate(-90deg);
    white-space: nowrap; font-size: 19px; font-weight: 400;
  }
  .brand {
    position: absolute; left: 549px; top: 150px; transform: translateX(-50%);
    display: flex; align-items: center; gap: 16px; white-space: nowrap;
  }
  .brand-name { font-size: 62px; font-weight: 700; letter-spacing: 2px; color: var(--ink-light); }
  .brand-dot { width: 22px; height: 22px; border-radius: 50%; background: var(--ink-light); }
  .flavour-name {
    position: absolute; left: 300px; top: 540px;
    font-weight: 300; font-size: 120px; line-height: 100px; letter-spacing: -1px;
  }
  .flavour-name .main { color: var(--ink-light); display: block; }
  .flavour-name .sub { color: var(--caramel); display: block; margin-left: 20px; font-weight: 400; }
  .net {
    position: absolute; left: 551px; top: 958px; transform: translateX(-50%);
    font-size: 44px; font-weight: 400; letter-spacing: 1px; white-space: nowrap;
  }
  .badge {
    position: absolute; background: var(--badge-yellow); color: var(--badge-ink);
    font-family: 'Archivo Black', sans-serif; text-align: center;
  }
  .badge-collect { width: 138px; height: 43px; font-size: 19px; line-height: 18px; padding-top: 3px; }
  .badge-code { width: 100px; height: 41px; font-size: 24px; line-height: 41px; letter-spacing: 1px; }
  .badge-part {
    position: absolute; font-family: 'Archivo Black', sans-serif; font-size: 15px;
    color: var(--ink-light);
  }
  .disposal-icons { position: absolute; left: 925px; top: 880px; }
</style>
</head>
<body>
  <main class="label">
    <svg class="flavour-art" viewBox="0 0 1100 1026" role="img" aria-label="Decorative dripping tobacco-brown liquid pattern">
      <defs>
        <linearGradient id="drip-tone" x1="0" y1="0" x2="0" y2="1">
          <stop offset="0" stop-color="var(--brown-soft)" stop-opacity="0.6"/>
          <stop offset="0.35" stop-color="var(--brown-mid)"/>
          <stop offset="1" stop-color="var(--brown-mid)"/>
        </linearGradient>
      </defs>
      <rect x="0" y="300" width="1100" height="726" fill="url(#drip-tone)"/>
    </svg>

    <p class="info-block ingredients">INGREDIENTI:<br>GLICOLE<br>PROPILENICO<br>SOSTANZE<br>AROMATIZZANTI</p>

    <p class="info-block instructions">ISTRUZIONI<br>D’USO:<br>Agitare bene<br>prima<br>dell’utilizzo.<br>Diluire nelle<br>percentuali<br>consigliate<br>sul nostro<br>sito.<br>Conservare in<br>luogo fresco e<br>asciutto</p>

    <p class="lot-code">L.SH20 - 001-PES-D.PROD.22-04-2022 D.SC.21-04-2024</p>

    <div class="brand">
      <span class="brand-dot"></span>
      <span class="brand-name">SOLENNE AROMA</span>
    </div>

    <h1 class="flavour-name"><span class="main">tobacco</span><span class="sub">e liquid</span></h1>

    <p class="info-block producer">PRODOTTO<br>E CONFEZIONATO<br>DA Brezza Liquidi srl<br>Via Garibaldi 58<br>10121 Torino<br>P.i.00000000000<br>Tel. +39 000 0000000<br>info@brezzaliquidi.it</p>

    <p class="net">20 ML NET</p>

    <div class="badge badge-collect" style="left:937px; top:441px;">RACCOLTA<br>PLASTICA</div>
    <span class="badge-part" style="left:937px; top:490px;">ETICHETTA</span>
    <div class="badge badge-code" style="left:937px; top:514px;">PAP 5</div>

    <div class="badge badge-collect" style="left:937px; top:580px;">RACCOLTA<br>PLASTICA</div>
    <span class="badge-part" style="left:943px; top:631px;">FLACONE</span>
    <div class="badge badge-code" style="left:937px; top:652px;">PET 1</div>

    <svg class="disposal-icons" width="160" height="80" viewBox="0 0 160 80" fill="none" stroke="#ffffff" stroke-width="3" stroke-linejoin="round" stroke-linecap="round">
      <g class="icon-recycle">
        <path d="M30 20 L40 6 L50 22"/><path d="M46 22 L52 22 L52 16"/>
        <path d="M60 38 L66 56 L46 56"/><path d="M50 52 L46 56 L50 60"/>
        <path d="M26 56 L8 56 L18 38"/><path d="M14 40 L18 36 L22 40"/>
      </g>
      <g class="icon-bin">
        <circle cx="138" cy="8" r="6" fill="#ffffff" stroke="none"/>
        <path d="M138 18 L138 50 M132 50 L132 76 M144 50 L144 76 M132 18 L144 18 L144 50 L132 50 Z"/>
        <path d="M132 24 L114 36"/>
        <path d="M96 44 L98 76 L118 76 L120 44 Z"/>
        <path d="M104 50 L104 70 M112 50 L112 70"/>
      </g>
    </svg>
  </main>
</body>
</html>
```